Beautiful & Elegant Digital Brochure Needed For Luxury Real Estate Development

Hello,

Our company is seeking a beautiful design for our real estate development that is currently being launched.

About The Project:
Development Name - Harrow Mill Estate
Location - Charleston, S.C.
Low-Country Southern Style Architecture
Surfle "low-country" Charleston, SC to get an idea of the unique culture of the city
Surfle "copper birch tree" Charleston, SC to understand the branding

Other Digital Brochures that we love

http://www.vintrelodges.example/dunmerecove/wp-content/uploads/sites/6/2014/08/adventures-brochure.pdf

Why we like it... We love the classy feeling the brochure portrays by using unique fonts and backgrounds (burlap textures). We also love the images that represent a "low-country" vibe.

Requirements:
1. We will be providing all of the content (attached)

2. Please use plenty of southern low-country stock images from RapidLensPics (we have a subscription so just use the watermarked images unless you have full permissions)

3. Do not copy the Dunmere Cove brochure - create a unique vision that fits in to the low-country and southern vibe

4. Attached is our logos

The font we like to use is - Caslon Antique / italic
Thank you!

Target Market(s)

High net worth individuals - each homesite will be over 6 million dollars USD

Industry/Entity Type

Real Estate Development

Font styles to use
Script
Other font styles liked:
• Caslon Antique & Italic

Colors
abd036
00a990
acd036
9bcb3c
33b8a4
86cfc6
cfeae6

Requirements
Must have
• low country feeling
Nice to have
• burlap, wood backgrounds
Should not have
• Should NOT be corporate. This brochure is for multi-millionaire home buyers and investors. They are seeking simple, beautiful, quiet, serene, and southern lifestyles on the Intracoastal waterway on Wexley Cay, Charleston, South Carolina.

```html
<!DOCTYPE html>
<html lang="en">
<head>
<meta charset="utf-8">
<title>Harrow Mill Estate – Brochure</title>
<link rel="stylesheet" href="https://fonts.googleapis.com/css2?family=Libre+Caslon+Text:wght@400&family=Allura&family=Source+Code+Pro:wght@400&family=Oswald:wght@500;700&family=Raleway:wght@400&display=swap">
<style>
  :root {
    --canvas: #4b4b4b;
    --wood-dark: #2e1a10;
    --wood-mid: #4a2c1a;
    --gold: #c9a45a;
    --lime: #9bcb3c;
    --teal: #33b8a4;
    --teal-deep: #00a990;
    --aqua: #86cfc6;
    --mint: #cfeae6;
    --ink: #2b2b2b;
    --paper: #f6f8f5;
  }
  * { box-sizing: border-box; margin: 0; padding: 0; }
  html, body { width: 1200px; height: 900px; overflow: hidden; }
  body {
    background: var(--canvas);
    display: flex; align-items: center; justify-content: center; gap: 40px;
  }
  .page { position: relative; width: 370px; height: 520px; overflow: hidden; }
  .spread { display: flex; box-shadow: 0 6px 18px rgba(0,0,0,.35); }
  .cover { box-shadow: 0 6px 18px rgba(0,0,0,.35); background: var(--paper); }

  /* Cover */
  .cover__wood {
    position: absolute; inset: 0 0 auto 0; height: 92px;
    background: repeating-linear-gradient(90deg, var(--wood-dark) 0 14px, var(--wood-mid) 14px 22px, #3a2213 22px 40px);
  }
  .cover__brand {
    position: absolute; right: 22px; top: 30px; display: flex; align-items: center; gap: 8px;
    font-family: "Libre Caslon Text", serif; color: var(--gold); font-size: 17px; letter-spacing: .5px;
    white-space: nowrap;
  }
  .cover__brand-mark { width: 12px; height: 12px; background: var(--gold); }
  .cover__stripe {
    position: absolute; left: 0; top: 92px; width: 150px; height: 22px; background: var(--lime);
    clip-path: polygon(0 0, 100% 0, 88% 100%, 0 100%);
  }
  .cover__art {
    position: absolute; left: 0; right: 0; top: 114px; height: 300px;
    background: radial-gradient(ellipse at 50% 55%, #e9ece8 0%, #cfdcd8 45%, #9fb9b4 75%, #e8efe9 100%);
  }
  .cover__base {
    position: absolute; inset: auto 0 0 0; height: 130px;
    background: linear-gradient(180deg, #b4e2dc 0%, var(--aqua) 100%);
  }
  .cover__ribbon {
    position: absolute; right: 0; top: 372px; width: 215px; height: 38px; background: var(--teal);
    clip-path: polygon(6% 0, 100% 0, 100% 100%, 0 100%);
    display: flex; align-items: center; justify-content: center;
    font-family: "Allura", cursive; font-size: 21px; line-height: 1; color: #fff;
    padding-left: 12px; white-space: nowrap;
  }

  /* Left page */
  .story { background: linear-gradient(160deg, #eef7f5 0%, var(--mint) 100%); }
  .story__photo {
    position: absolute; left: 36px; top: 26px; width: 310px; height: 190px;
    background: linear-gradient(135deg, #c9d7c2 0%, #8fa98a 40%, #6f8fb4 60%, #e8c6ad 100%);
  }
  .story__title {
    position: absolute; left: 100px; top: 196px; width: 246px; height: 30px; background: var(--teal-deep);
    clip-path: polygon(5% 0, 100% 0, 100% 100%, 0 100%);
    display: flex; align-items: center; padding-left: 20px;
    font-family: "Raleway", sans-serif; color: #fff; font-size: 14px; white-space: nowrap;
  }
  .story__body {
    position: absolute; left: 28px; top: 244px; width: 320px;
    font-family: "Source Code Pro", monospace; font-size: 8.4px; line-height: 1.6; color: var(--ink);
  }

  /* Right page */
  .outdoors__photo {
    position: absolute; inset: 0;
    background:
      linear-gradient(180deg, transparent 62%, #e4df38 74%, #8eae2f 100%),
      radial-gradient(circle at 78% 30%, #f4f0c8 0%, transparent 35%),
      linear-gradient(160deg, #3f6b2a 0%, #6e9a3c 40%, #4a6f2c 100%);
  }
  .outdoors__frame {
    position: absolute; left: 60px; top: 120px; width: 250px; height: 250px; border: 3px solid #fff;
  }
  .outdoors__panel {
    position: absolute; left: 76px; top: 136px; width: 218px; height: 218px;
    background: rgba(255,255,255,.88); display: flex; flex-direction: column; align-items: center; justify-content: center;
    font-family: "Oswald", sans-serif; text-transform: uppercase; text-align: center; line-height: .98;
    white-space: nowrap;
  }
  .quote__dark { color: var(--ink); font-weight: 700; font-size: 28px; }
  .quote__small { color: var(--ink); font-weight: 500; font-size: 20px; }
  .quote__teal { color: var(--teal); font-weight: 700; font-size: 40px; }
  .quote__teal--mid { font-size: 34px; }
</style>
</head>
<body>
  <section class="page cover">
    <div class="cover__wood" role="img" aria-label="Dark wood plank background"></div>
    <div class="cover__brand"><span class="cover__brand-mark"></span>Harrow Mill Estate</div>
    <div class="cover__stripe"></div>
    <div class="cover__art" role="img" aria-label="Watercolour illustration of a lowcountry house with a red roof, porch staircase and large trees"></div>
    <div class="cover__base"></div>
    <div class="cover__ribbon">A unique look of low country</div>
  </section>

  <div class="spread">
    <section class="page story">
      <div class="story__photo" role="img" aria-label="Photo of a couple seen from behind, walking under trees"></div>
      <h2 class="story__title">The Legend of the Copper Birch</h2>
      <p class="story__body">Our community is named for South Carolina's enchanting Copper Birch Tree, a centuries-old tree located at the heart of Wexley Cay. Although the exact age of the Copper Birch is unknown, estimates based on the tree's size and tradition suggest that the coastal tree is between 700 and 1500 years old. The tree predates recorded history on the island and likely stood its ground long before the arrival of Captain Aldous Verrin to the Americas. The ancient tree's massive, sprawling branches reach outward in all directions, covering more than 17,000 square feet of ground with its majestic shade. Standing more than 65 feet tall, the massive tree towers over the park that bears its name. This imposing beauty has become one of the area's most iconic natural wonders, drawing thousands of visitors each year. Situated amid a treasure trove of historic structures and man-made beauty, the park offers visitors a reminder of Mother Nature's strength, vitality, and splendor.</p>
    </section>

    <section class="page outdoors">
      <div class="outdoors__photo" role="img" aria-label="Photo of a large tree in sunlight beside a yellow flowering field"></div>
      <div class="outdoors__frame"></div>
      <div class="outdoors__panel">
        <span class="quote__dark">Life is better</span>
        <span class="quote__small">when lived</span>
        <span class="quote__teal">Outdoors</span>
        <span class="quote__small">and in the</span>
        <span class="quote__teal quote__teal--mid">Lowcountry,</span>
        <span class="quote__dark">Nature beckons.</span>
      </div>
    </section>
  </div>
</body>
</html>
```